Quorvan Medical business cards

Double sided business cards.

Medical technology consulting company.

Business cards with two names on the front, upper to middle left:

Dr Colin R. Harbury BMed GAICD +61412558907
Dr Owen Palatsky PhD MCommrclLaw +61437619042

Email and website addresses bottom right:

colin@quorvanmedical.com.au
www.quorvanmedical.com.au

Tree logo (as per attached file) on front in a suitable position.

Tag line (as per attached files) on the back.

Need a file format to upload to Paper Haven or Cardlyner.

```html
<!DOCTYPE html>
<html lang="en">
<head>
<meta charset="utf-8">
<title>Quorvan Medical business cards</title>
<link rel="stylesheet" href="https://fonts.googleapis.com/css2?family=Montserrat:wght@400;500;700;800&display=swap">
<style>
  :root {
    --stage: #a3a6a5;
    --card: #ffffff;
    --green: #4c8f3e;
    --maroon: #6e1a18;
    --ink: #1c1c1c;
    --rule: #222222;
  }
  * { box-sizing: border-box; margin: 0; padding: 0; }
  html, body { width: 1200px; height: 931px; overflow: hidden; }
  body {
    background: var(--stage);
    font-family: "Montserrat", sans-serif;
    position: relative;
  }
  .card {
    position: absolute;
    width: 700px;
    height: 400px;
    background: var(--card);
    box-shadow: 0 6px 18px rgba(0,0,0,0.25);
    overflow: hidden;
  }
  /* Back: appointment reminder */
  .card-back { left: 60px; top: 40px; }
  .brand-mark {
    position: absolute; right: 48px; top: 34px;
    display: flex; align-items: center; gap: 8px;
    color: var(--green); font-weight: 500; font-size: 17px; letter-spacing: 0.5px;
  }
  .brand-mark .dot { width: 14px; height: 14px; border-radius: 50%; background: var(--green); }
  .reminder-title { position: absolute; left: 48px; top: 110px; }
  .reminder-title h2 { color: var(--green); font-weight: 800; font-size: 26px; }
  .reminder-title p { color: var(--ink); font-size: 14px; margin-top: 2px; }
  .fields { position: absolute; left: 96px; top: 180px; width: 540px; }
  .field { display: flex; align-items: flex-end; gap: 8px; height: 44px; color: var(--ink); font-size: 15px; }
  .field .line { flex: 1; border-bottom: 1.5px solid var(--rule); height: 1px; margin-bottom: 4px; }
  .field .unit { font-size: 13px; }
  .tagline {
    position: absolute; right: 48px; bottom: 40px;
    color: var(--green); font-size: 30px; font-weight: 400; letter-spacing: 0.5px;
  }
  .tagline .sep { color: var(--maroon); margin: 0 8px; }

  /* Front: names and contact */
  .card-front { left: 440px; top: 491px; }
  .wordmark {
    position: absolute; left: 44px; top: 70px;
    color: var(--green); font-weight: 500; font-size: 50px; letter-spacing: 1px;
  }
  .people { position: absolute; left: 50px; top: 160px; }
  .person { margin-bottom: 14px; }
  .person .name { color: var(--green); font-weight: 800; font-size: 21px; }
  .person .phone { display: flex; align-items: center; gap: 10px; margin-top: 6px; font-size: 15px; color: var(--ink); padding-left: 16px; }
  .person .phone svg { width: 18px; height: 18px; }
  .contact-band {
    position: absolute; left: 0; right: 0; bottom: 0; height: 68px;
    background: var(--green); color: #fff;
    display: flex; align-items: center; justify-content: flex-end; gap: 22px;
    padding-right: 40px; font-size: 15px;
  }
  .contact-band .divider { width: 1px; height: 28px; background: rgba(255,255,255,0.8); }
</style>
</head>
<body>

<section class="card card-back">
  <div class="brand-mark"><span class="dot"></span>Quorvan Medical</div>
  <div class="reminder-title">
    <h2>Apointment</h2>
    <p>Reminder</p>
  </div>
  <div class="fields">
    <div class="field"><span>Name</span><span class="line"></span></div>
    <div class="field"><span>Date</span><span class="line"></span><span class="unit">am/pm</span></div>
    <div class="field"><span>Time</span><span class="line"></span></div>
  </div>
  <p class="tagline">Concept<span class="sep">|</span>Commercialisation<span class="sep">|</span>Beyond</p>
</section>

<section class="card card-front">
  <h1 class="wordmark">QUORVAN MEDICAL</h1>
  <div class="people">
    <div class="person">
      <p class="name">Dr Colin R. Harbury BMed GAICD</p>
      <p class="phone">
        <svg viewBox="0 0 24 24" aria-hidden="true"><path fill="#4c8f3e" d="M6.6 10.8a15 15 0 0 0 6.6 6.6l2.2-2.2c.3-.3.7-.4 1-.2 1.1.4 2.3.6 3.6.6.6 0 1 .4 1 1V20c0 .6-.4 1-1 1A17 17 0 0 1 3 4c0-.6.4-1 1-1h3.5c.6 0 1 .4 1 1 0 1.3.2 2.5.6 3.6.1.3 0 .7-.2 1z"/></svg>
        +61412558907
      </p>
    </div>
    <div class="person">
      <p class="name">Dr Owen Palatsky PhD MCommrclLaw</p>
      <p class="phone">
        <svg viewBox="0 0 24 24" aria-hidden="true"><path fill="#4c8f3e" d="M6.6 10.8a15 15 0 0 0 6.6 6.6l2.2-2.2c.3-.3.7-.4 1-.2 1.1.4 2.3.6 3.6.6.6 0 1 .4 1 1V20c0 .6-.4 1-1 1A17 17 0 0 1 3 4c0-.6.4-1 1-1h3.5c.6 0 1 .4 1 1 0 1.3.2 2.5.6 3.6.1.3 0 .7-.2 1z"/></svg>
        +61437619042
      </p>
    </div>
  </div>
  <div class="contact-band">
    <span>colin@quorvanmedical.com.au</span>
    <span class="divider"></span>
    <span>www.quorvanmedical.com.au</span>
  </div>
</section>

</body>
</html>
```